Infographic - post exit survey

An infographic is required for the top of some marketing collateral on the topic of 'post exit survey'. This survey is conducted for ex-employees who have left the organisation after a period of at least 1 month. The infographic needs to be clear, simple and easy to understand without too many words. Graphics need to be kept simple whilst utilising the LUMV brand colours.
Target Market(s)
Commercial, non for profit, aged care and disability sectors
Industry/Entity Type
Marketing
Font styles to use
Sans Serif
Colors
0355a3
3176b5
85acd3
cedeed
e34197
Requirements
Must have
- We are a HR consulting firm so this must be professional and to the point. We want it to be clear, concise and to the point. Not too heavy on the text. Please use LUMV Consulting colors. You can find our color scheme on our website: lumvadvise.com.au

```html
<!DOCTYPE html>
<html lang="en">
<head>
<meta charset="utf-8">
<title>Post Exit Survey information</title>
<link href="https://fonts.googleapis.com/css2?family=Open+Sans:ital,wght@0,700;0,800;1,600&display=swap" rel="stylesheet">
<style>
  :root {
    --navy: #0355a3;
    --mid-blue: #3176b5;
    --light-blue: #85acd3;
    --pale-blue: #cedeed;
    --pink: #e34197;
    --deep: #1f4b9c;
    --body-text: #d4e2f2;
  }
  * { margin: 0; padding: 0; box-sizing: border-box; }
  html, body { width: 1200px; height: 865px; overflow: hidden; background: var(--deep); }
  .infographic {
    position: relative;
    width: 1200px;
    height: 865px;
    overflow: hidden;
    font-family: "Open Sans", Arial, sans-serif;
    background:
      radial-gradient(ellipse 520px 420px at 600px 390px, #7fbde9 0%, #4e8fcf 45%, rgba(49,118,181,0) 100%),
      linear-gradient(180deg, #2b5cab 0%, #3a6fb9 40%, #2a5aa9 75%, #1f4b9c 100%);
  }
  .sweep { position: absolute; inset: 0; }
  .side-rail {
    position: absolute; left: 60px; top: 0; width: 32px; height: 865px;
    background: var(--pale-blue);
  }
  .accent-line {
    position: absolute; left: 98px; top: 156px; width: 1038px; height: 13px;
    background: var(--pink); border-radius: 7px;
  }
  .title-bar {
    position: absolute; left: 92px; top: 178px; width: 1062px; height: 116px;
    background: var(--pale-blue); border-radius: 0 22px 22px 0;
  }
  .title {
    position: absolute; left: 132px; top: 188px;
    font-weight: 800; font-size: 66px; letter-spacing: -0.5px;
    color: var(--navy); line-height: 96px;
  }
  .body-copy {
    position: absolute; left: 132px; top: 318px; width: 960px;
    font-weight: 700; font-size: 21.5px; line-height: 29.5px;
    color: var(--body-text);
  }
  .body-copy p + p { margin-top: 28px; }
  .drop-cap { font-size: 40px; line-height: 20px; }
  .note { font-style: italic; font-weight: 600; }
  .brand, .term { color: var(--navy); }
  .term-soft { color: #ffffff; }
</style>
</head>
<body>
<div class="infographic">
  <svg class="sweep" width="1200" height="865" viewBox="0 0 1200 865" aria-hidden="true">
    <path d="M1200 0 L1200 865 L330 865 C760 780 1130 470 1200 0 Z" fill="#ffffff" opacity="0.12"/>
    <path d="M1200 0 C1120 470 760 790 300 865 L1200 865 Z" fill="#1f4b9c" opacity="0.25"/>
  </svg>
  <div class="side-rail"></div>
  <div class="accent-line"></div>
  <div class="title-bar"></div>
  <h1 class="title">Post Exit Survey information</h1>
  <div class="body-copy">
    <p><span class="drop-cap">A</span>fter the employee has ceased employment (<span class="note">minimum 1 month later</span>),<br>
    they will receive an email from <span class="brand">LUMV</span> Consulting, inviting them to complete a<br>
    quick <span class="term-soft">Post Exit Survey.</span> When we have compared responses from a standard</p>
    <p><span class="term">Exit Survey</span> versus a <span class="term">Post Exit Survey</span> for the same organisation the<br>
    responseswere markedly different. People are more likely to be more honest<br>
    once they have been away from the organisation&nbsp; for a period of time, and<br>
    are more likely to respond when it is delivered&nbsp; by an impartial third party.<br>
    The post exit survey consists of a 10 question questionnaire In order to pro-<br>
    tect confidentiality a minimum of 3 exit surveys must be completed&nbsp; before<br>
    any data is provided to the organisation Responses a graphed against the<br>
    10 main reasons why people leave their jobs.</p>
  </div>
</div>
</body>
</html>
```